New web page, 2 companies on the one page

A new web page for an engineering consultancy and maintenance management company

Corrick & Associates is the parent company covering the design and consultancy
Trivolt Engineering is the Maintenance and Reliability company

Target Market(s)

Food & Beverage, ingredients Manufacturing
engineering managers

Coding

Coded - Design and coding required

Number of Pages Required

1 page

Font styles to use
Other font styles liked:
• Roboto

Colors
1861ab
85acd3
d0dfed
cee9f5

```html
<!DOCTYPE html>
<html lang="en">
<head>
<meta charset="utf-8">
<title>Corrick &amp; Associates | Trivolt Engineering</title>
<link href="https://fonts.googleapis.com/css2?family=Lato:wght@400;700;900&family=Roboto:wght@400;500;700&display=swap" rel="stylesheet">
<style>
:root{
  --brand:#1861ab;
  --brand-light:#85acd3;
  --pale:#d0dfed;
  --pale-cyan:#cee9f5;
  --navy:#1d3558;
  --ink:#222;
  --muted:#555;
  --footer:#262626;
  --white:#fff;
}
*{margin:0;padding:0;box-sizing:border-box}
html,body{width:1200px;height:2912px;overflow:hidden}
body{position:relative;background:var(--white);font-family:Roboto,Arial,sans-serif;color:var(--ink)}
.abs{position:absolute}
.btn{position:absolute;display:flex;align-items:center;justify-content:center;width:180px;height:46px;border-radius:23px;background:var(--brand-light);color:var(--white);font:700 14px Lato,sans-serif;letter-spacing:1.5px}

/* header */
.site-header{position:absolute;left:0;top:0;width:1200px;height:112px;background:var(--white);box-shadow:0 2px 6px rgba(0,0,0,.12);z-index:2}
.brand{position:absolute;top:33px;display:flex;align-items:center;gap:10px;font:900 20px/1 Lato,sans-serif;color:var(--navy);white-space:nowrap}
.brand .dot{width:46px;height:46px;border-radius:50%;background:var(--brand);flex:none}
.brand-parent{left:20px}
.brand-sub{left:336px;top:40px;flex-direction:column;align-items:flex-start;gap:4px;padding-left:16px;border-left:2px solid var(--pale)}
.brand-sub small{font:700 10px/1 Lato,sans-serif;color:var(--brand);letter-spacing:1px}
.main-nav{position:absolute;right:40px;top:48px;display:flex;gap:34px;font:500 14px Roboto,sans-serif;letter-spacing:1px;white-space:nowrap}
.main-nav span{color:var(--navy)}
.main-nav .active{color:var(--brand-light)}

/* hero */
.hero{position:absolute;left:0;top:112px;width:1200px;height:668px;background:linear-gradient(120deg,#6d6459 0%,#a49a8c 25%,#5d6670 55%,#cfc8bf 80%,#7c7d80 100%)}
.hero::after{content:"";position:absolute;inset:0;background:rgba(20,30,45,.35)}
.hero-copy{position:absolute;left:0;top:205px;width:1200px;text-align:center;color:var(--white);z-index:1}
.hero-copy h1{font:900 46px/1.1 Lato,sans-serif;letter-spacing:1px}
.hero-copy p{width:520px;margin:22px auto 0;font:400 16px/1.45 Roboto,sans-serif}
.hero .btn{left:510px;top:400px;z-index:1}
.slider-dots{position:absolute;left:40px;top:604px;display:flex;gap:10px;z-index:1}
.slider-dots i{width:12px;height:12px;border-radius:50%;background:rgba(255,255,255,.5)}
.slider-dots i:first-child{background:var(--white)}

/* about */
.about-photo{position:absolute;left:190px;top:852px;width:402px;height:440px;background:linear-gradient(135deg,#3f5a78,#8ba3b8 50%,#c9c2b5)}
.about-copy{position:absolute;left:614px;top:852px;width:520px}
.about-copy h2{font:900 38px/1.08 Lato,sans-serif;color:var(--navy)}
.about-copy p{margin-top:14px;font:400 15px/1.55 Roboto,sans-serif;color:var(--ink)}
.about .btn{left:614px;top:1238px}

/* services */
.services{position:absolute;left:0;top:1360px;width:1200px;height:720px;background:linear-gradient(180deg,var(--pale) 0%,#eef5fb 50%,var(--pale) 100%)}
.section-title{position:absolute;left:0;width:1200px;text-align:center;font:900 38px Lato,sans-serif;color:var(--navy)}
.services svg{position:absolute;left:0;top:0}
.service-label{position:absolute;width:300px;font:700 15px/1.35 Roboto,sans-serif;color:var(--navy)}
.service-label.left{text-align:right}
.hub-name{position:absolute;left:500px;top:312px;width:200px;text-align:center;font:900 18px/1.2 Lato,sans-serif;color:var(--brand)}
.services .btn{left:510px;top:614px}

/* news */
.news-card{position:absolute;top:2212px;width:328px}
.news-photo{height:196px;border-radius:4px}
.news-card h3{margin-top:38px;text-align:center;font:900 17px Lato,sans-serif;color:var(--navy)}
.news-card p{margin-top:10px;text-align:center;font:400 13px/1.45 Roboto,sans-serif;color:var(--muted)}
.news-card a{display:block;margin-top:14px;text-align:center;font:500 14px Roboto,sans-serif;color:var(--brand);text-decoration:none}

/* footer */
.site-footer{position:absolute;left:0;top:2690px;width:1200px;height:222px;background:var(--footer)}
.footer-badge{position:absolute;left:556px;top:-34px;width:88px;height:88px;border-radius:50%;background:var(--white);display:flex;align-items:center;justify-content:center}
.footer-badge span{width:56px;height:56px;border-radius:50%;background:var(--brand)}
.footer-nav{position:absolute;left:0;top:92px;width:1200px;display:flex;justify-content:center;gap:34px;font:500 14px Roboto,sans-serif;color:var(--white);letter-spacing:1px}
.social{position:absolute;left:0;top:128px;width:1200px;display:flex;justify-content:center;gap:22px}
.social i{width:18px;height:18px;border-radius:50%;background:var(--white)}
.copyright{position:absolute;left:0;top:170px;width:1200px;text-align:center;font:400 12px Roboto,sans-serif;color:#aaa}
</style>
</head>
<body>

<header class="site-header">
  <div class="brand brand-parent"><span class="dot"></span><span>CORRICK &amp; ASSOCIATES</span></div>
  <div class="brand brand-sub"><span>TRIVOLT</span><small>ENGINEERING</small></div>
  <nav class="main-nav">
    <span class="active">HOME</span><span>ABOUT US</span><span>SERVICES</span><span>LATEST NEWS</span><span>CONTACT US</span>
  </nav>
</header>

<section class="hero">
  <div class="abs" style="inset:0" role="img" aria-label="Engineering team meeting around a table with hard hats and laptops"></div>
  <div class="hero-copy">
    <h1>WELCOME TO<br>CORRICK &amp; ASSOCIATES</h1>
    <p>Excepteur sint occaecat cupidatat non proident, sunt in culpa qui officia deserunt mollit anim id est laborum.</p>
  </div>
  <span class="btn">READ MORE</span>
  <div class="slider-dots"><i></i><i></i><i></i></div>
</section>

<section class="about">
  <div class="about-photo" role="img" aria-label="Engineer in a hard hat shaking hands in a plant room"></div>
  <div class="about-copy">
    <h2>ABOUT<br>CORRICK &amp; ASSOCIATES</h2>
    <p>Corrick &amp; Associates is specialised manufacturing engineering support organisation that can provide fast, nimble, and flexible services.</p>
    <p>We have a proven track record in delivering tangible outcomes in process design and fit-out, project management, manufacturing process and maintenance design and execution.</p>
    <p>Our specialist focus in food manufacturing across a range of sectors allows our team to deliver real benefits to performance and recognition of the clients investment.</p>
  </div>
  <span class="btn">READ MORE</span>
</section>

<section class="services">
  <h2 class="section-title" style="top:54px">OUR SERVICES</h2>
  <svg width="1200" height="720" viewBox="0 0 1200 720">
    <circle cx="600" cy="330" r="176" fill="none" stroke="#85acd3" stroke-width="3" opacity=".6"/>
    <circle cx="600" cy="330" r="150" fill="#fff" stroke="#d0dfed" stroke-width="6"/>
    <circle cx="600" cy="330" r="104" fill="#eef2f6" stroke="#1861ab" stroke-width="3"/>
    <g fill="#1d3558" stroke="#85acd3" stroke-width="5">
      <circle cx="468" cy="176" r="26"/>
      <circle cx="416" cy="340" r="26"/>
      <circle cx="468" cy="488" r="26"/>
      <circle cx="732" cy="176" r="26"/>
      <circle cx="784" cy="340" r="26"/>
      <circle cx="732" cy="488" r="26"/>
    </g>
    <g fill="none" stroke="#fff" stroke-width="2.5" stroke-linecap="round">
      <rect x="460" y="166" width="16" height="20" rx="2"/><path d="M464 173h8M464 179h8"/>
      <circle cx="416" cy="335" r="5"/><path d="M407 350q9-10 18 0"/>
      <path d="M460 496l14-14M472 480l6-2-2 6"/>
      <circle cx="727" cy="172" r="4"/><circle cx="738" cy="181" r="4"/><path d="M720 186q7-6 14 0"/>
      <path d="M776 348l16-16M778 334l6 6"/>
      <circle cx="728" cy="484" r="5"/><circle cx="739" cy="494" r="3"/>
    </g>
  </svg>
  <div class="hub-name">CORRICK &amp;<br>ASSOCIATES</div>
  <div class="service-label left" style="left:108px;top:158px">Process &amp;<br>Facilities Design</div>
  <div class="service-label left" style="left:56px;top:322px">Project<br>Management</div>
  <div class="service-label left" style="left:100px;top:480px">Major Equipment and Services<br>Installation &amp; Commissioning</div>
  <div class="service-label" style="left:804px;top:158px">Engineering &amp; Maintenance<br>Management</div>
  <div class="service-label" style="left:852px;top:322px">Maintenance<br>Execution</div>
  <div class="service-label" style="left:804px;top:480px">Manufacturing Performance<br>Measurement</div>
  <span class="btn">READ MORE</span>
</section>

<section class="news">
  <h2 class="section-title" style="top:2126px">LATEST NEWS</h2>
  <article class="news-card" style="left:72px">
    <div class="news-photo" role="img" aria-label="Engineer at a desk with monitors showing schedules" style="background:linear-gradient(135deg,#5a6d80,#b8c6d2)"></div>
    <h3>LOREM IPSUM DOLOR SIT AMET</h3>
    <p>Consectetur adipiscing elit, sed do eiusmod tempor incididunt ut labore et dolore magna aliqua, quis nostrud.</p>
    <a>Continue Reading</a>
  </article>
  <article class="news-card" style="left:436px">
    <div class="news-photo" role="img" aria-label="Technicians working on industrial machinery" style="background:linear-gradient(135deg,#2f4a66,#7f97ad 60%,#c7a77a)"></div>
    <h3>LOREM IPSUM DOLOR SIT AMET</h3>
    <p>Consectetur adipiscing elit, sed do eiusmod tempor incididunt ut labore et dolore magna aliqua, quis nostrud.</p>
    <a>Continue Reading</a>
  </article>
  <article class="news-card" style="left:800px">
    <div class="news-photo" role="img" aria-label="Engineer with a laptop in a factory" style="background:linear-gradient(135deg,#6a6e73,#c9ccd0)"></div>
    <h3>LOREM IPSUM DOLOR SIT AMET</h3>
    <p>Consectetur adipiscing elit, sed do eiusmod tempor incididunt ut labore et dolore magna aliqua, quis nostrud.</p>
    <a>Continue Reading</a>
  </article>
</section>

<footer class="site-footer">
  <div class="footer-badge"><span></span></div>
  <nav class="footer-nav"><span>HOME</span><span>ABOUT US</span><span>SERVICES</span><span>LATEST NEWS</span><span>CONTACT US</span></nav>
  <div class="social"><i></i><i></i><i></i><i></i></div>
  <p class="copyright">Copyright ©2022 Company Name. All Rights Reserved</p>
</footer>

</body>
</html>
```